PROPERTY MANAGEMENT AND REAL ESTATE

Target Market(s)

real estate owners and investors

Industry/Entity Type

Real Estate

Contact Information for Business Card

BRIGHT LANTERN PROPERTY MANAGEMENT GROUP, LLC
487 Corwin Lane
Unit 260
Seabright Cove, FL 33127

```html
<!DOCTYPE html>
<html lang="en">
<head>
<meta charset="utf-8">
<title>Bright Lantern Property Management Group – Business Card</title>
<link rel="stylesheet" href="https://fonts.googleapis.com/css2?family=Raleway:wght@400;500;600&display=swap">
<style>
  :root {
    --brand-red: #8c1519;
    --paper: #f7f6f4;
    --paper-shade: #ecebe8;
    --ink-light: #ffffff;
    --ink-muted: #6d6d6d;
    --backdrop: #d6d6d4;
  }
  * { box-sizing: border-box; margin: 0; padding: 0; }
  html, body {
    width: 1200px; height: 1200px; overflow: hidden;
    background: var(--backdrop);
    font-family: "Raleway", sans-serif;
  }
  .sheet {
    width: 1200px; height: 1200px;
    display: flex; flex-direction: column; align-items: center; justify-content: center;
    gap: 60px;
  }
  .card {
    position: relative;
    width: 840px; height: 480px;
    background: var(--paper);
    box-shadow: 0 4px 14px rgba(0,0,0,0.18);
    overflow: hidden;
  }

  /* Front */
  .card-front .building-art {
    position: absolute; left: 250px; top: 130px;
    width: 300px; height: 350px;
    background: linear-gradient(180deg, var(--paper-shade), #e4e2df);
    opacity: 0.8;
  }
  .brand {
    position: absolute; left: 40px; top: 36px;
    display: flex; align-items: center; gap: 14px;
  }
  .brand-mark {
    width: 44px; height: 44px; border-radius: 50%;
    background: var(--brand-red);
  }
  .brand-name {
    color: var(--ink-muted);
    font-size: 15px; font-weight: 500;
    letter-spacing: 0.08em; line-height: 1.3;
    text-transform: uppercase;
  }
  .name-band {
    position: absolute; left: 0; top: 148px;
    width: 500px; height: 72px;
    background: var(--brand-red);
    display: flex; align-items: center;
    padding-left: 40px;
  }
  .person-name {
    color: var(--ink-light);
    font-size: 40px; font-weight: 500; letter-spacing: 0.04em;
  }
  .contact-panel {
    position: absolute; right: 0; top: 0;
    width: 250px; height: 100%;
    background: var(--brand-red);
    color: var(--ink-light);
    display: flex; flex-direction: column; align-items: flex-end; justify-content: space-between;
    padding: 48px 22px 40px 16px;
    text-align: right;
  }
  .contact-group { display: flex; flex-direction: column; align-items: flex-end; gap: 10px; }
  .contact-icon { width: 30px; height: 30px; align-self: center; }
  .contact-text { font-size: 13px; line-height: 1.5; white-space: nowrap; }
  .contact-text.phone { font-size: 17px; letter-spacing: 0.04em; }

  /* Back */
  .card-back { border: 22px solid var(--brand-red); display: flex; align-items: center; justify-content: center; }
  .back-brand {
    display: flex; flex-direction: column; align-items: center; gap: 22px;
  }
  .back-mark { width: 120px; height: 120px; border-radius: 50%; background: var(--brand-red); }
  .back-name {
    color: var(--brand-red);
    font-size: 22px; font-weight: 600; letter-spacing: 0.1em;
    text-align: center; line-height: 1.35; text-transform: uppercase;
  }
</style>
</head>
<body>
<main class="sheet">

  <section class="card card-front">
    <div class="building-art" role="img" aria-label="Faint illustration of an apartment building"></div>

    <div class="brand">
      <span class="brand-mark"></span>
      <p class="brand-name">Bright Lantern Property<br>Management Group, LLC</p>
    </div>

    <div class="name-band">
      <h1 class="person-name">JOHN DOE</h1>
    </div>

    <aside class="contact-panel">
      <div class="contact-group">
        <svg class="contact-icon" viewBox="0 0 24 24" aria-hidden="true">
          <path d="M12 2a7 7 0 0 0-7 7c0 5 7 13 7 13s7-8 7-13a7 7 0 0 0-7-7zm0 9.5A2.5 2.5 0 1 1 12 6.5a2.5 2.5 0 0 1 0 5z" fill="#fff"/>
        </svg>
        <p class="contact-text">487 Corwin Lane, Unit 260<br>Seabright Cove, FL 33127</p>
      </div>

      <div class="contact-group">
        <svg class="contact-icon" viewBox="0 0 24 24" aria-hidden="true">
          <path d="M6.6 10.8a15.1 15.1 0 0 0 6.6 6.6l2.2-2.2a1 1 0 0 1 1-.25 11.4 11.4 0 0 0 3.6.57 1 1 0 0 1 1 1V20a1 1 0 0 1-1 1A17 17 0 0 1 3 4a1 1 0 0 1 1-1h3.5a1 1 0 0 1 1 1c0 1.25.2 2.45.57 3.57a1 1 0 0 1-.25 1z" fill="#fff"/>
        </svg>
        <p class="contact-text phone">(954) 555-0148<br>(954) 555-0149</p>
      </div>

      <div class="contact-group">
        <svg class="contact-icon" viewBox="0 0 24 24" aria-hidden="true" fill="none" stroke="#fff" stroke-width="1.6">
          <circle cx="12" cy="12" r="9"/>
          <ellipse cx="12" cy="12" rx="4" ry="9"/>
          <line x1="3" y1="12" x2="21" y2="12"/>
        </svg>
        <p class="contact-text">name@brightlanternpm.com<br>www.brightlanternpm.com</p>
      </div>
    </aside>
  </section>

  <section class="card card-back">
    <div class="back-brand">
      <span class="back-mark"></span>
      <p class="back-name">Bright Lantern Property<br>Management Group, LLC</p>
    </div>
  </section>

</main>
</body>
</html>
```